Korvane Works Business cards

We require somebody to design business cards for our new business.

Target Market(s)

Mining, haulage and civil.

Industry/Entity Type

Auto electrician in mining industry

Contact Information for Business Card

ABN, business email address, mobile number.

Colors
00AB8E
00BBA5
67D7C9
C6EFE9
E9F9F6

Requirements
Must have
• Services I offer: Breakdowns, Field Service, A/C Systems, Machine rewires, mine site vehicle fit outs

```html
<!DOCTYPE html>
<html lang="en">
<head>
<meta charset="utf-8">
<title>Korvane Works — Business Cards</title>
<link rel="stylesheet" href="https://fonts.googleapis.com/css2?family=Rajdhani:wght@600;700&family=Fira+Sans:wght@400&display=swap">
<style>
  :root {
    --bg: #e4e4e4;
    --card-light: #ffffff;
    --card-dark-top: #3c3c3c;
    --card-dark-bottom: #2b2b2b;
    --teal: #5ccfc3;
    --teal-deep: #00bba5;
    --ink: #4a4a4a;
    --muted: #6b6b6b;
    --silver: #bdbdbd;
    --rule: #c9c9c9;
  }
  * { box-sizing: border-box; margin: 0; padding: 0; }
  html, body { width: 1200px; height: 1200px; overflow: hidden; }
  body { background: var(--bg); position: relative; font-family: "Fira Sans", sans-serif; }

  .card {
    position: absolute;
    left: 265px;
    width: 688px;
    height: 393px;
    border-radius: 20px;
    box-shadow: 0 10px 24px rgba(0,0,0,0.18);
    overflow: hidden;
  }
  .card--front { top: 159px; background: var(--card-light); }
  .card--back {
    top: 653px;
    background: linear-gradient(180deg, var(--card-dark-top), var(--card-dark-bottom));
    display: flex; flex-direction: column; align-items: center; justify-content: center; gap: 22px;
  }

  .brand {
    display: flex; align-items: center; gap: 12px;
    font-family: "Rajdhani", sans-serif; font-weight: 700;
    color: var(--teal); text-transform: uppercase; letter-spacing: 1px; white-space: nowrap;
  }
  .brand__dot { border-radius: 50%; background: var(--teal); flex: none; }
  .card--front .brand {
    position: absolute; left: 30px; width: 300px; top: 175px;
    justify-content: center; font-size: 32px;
  }
  .card--front .brand__dot { width: 16px; height: 16px; }
  .card--back .brand { font-size: 56px; }
  .card--back .brand__dot { width: 28px; height: 28px; }

  .services {
    list-style: none; display: flex; flex-wrap: wrap; justify-content: center;
    width: 520px; row-gap: 8px;
    font-family: "Rajdhani", sans-serif; font-weight: 600;
    font-size: 15px; letter-spacing: 3px; text-transform: uppercase; color: var(--silver);
  }
  .services li { white-space: nowrap; }
  .services li + li::before { content: "·"; margin: 0 10px; color: var(--teal); }

  .divider {
    position: absolute; left: 345px; top: 85px;
    width: 2px; height: 235px; background: var(--rule);
  }

  .contact { position: absolute; left: 370px; top: 82px; color: var(--ink); }
  .contact__name {
    font-family: "Rajdhani", sans-serif; font-weight: 700;
    font-size: 29px; line-height: 1; color: var(--teal); text-transform: uppercase;
  }
  .contact__role { font-size: 15px; color: var(--muted); margin-top: 4px; }
  .contact__address { font-size: 16px; line-height: 21px; margin-top: 18px; }
  .contact__list { list-style: none; margin-top: 10px; }
  .contact__list li {
    display: flex; align-items: center; gap: 12px;
    font-size: 16px; line-height: 20px; height: 21px; white-space: nowrap;
  }
  .contact__list svg { width: 14px; height: 14px; fill: var(--teal-deep); flex: none; }
  .contact__abn { font-size: 14px; color: var(--muted); margin-top: 8px; letter-spacing: 0.5px; }
</style>
</head>
<body>

<section class="card card--front" aria-label="Business card front">
  <div class="brand"><span class="brand__dot"></span>Korvane Works</div>
  <div class="divider"></div>
  <div class="contact">
    <h1 class="contact__name">Dana Pryor</h1>
    <p class="contact__role">President</p>
    <p class="contact__address">412 Ironbark Road<br>Redmarsh, Canada 30812</p>
    <ul class="contact__list">
      <li>
        <svg viewBox="0 0 24 24" aria-hidden="true"><path d="M6.6 10.8a15 15 0 0 0 6.6 6.6l2.2-2.2c.3-.3.7-.4 1-.2 1.1.4 2.3.6 3.6.6.6 0 1 .4 1 1V20c0 .6-.4 1-1 1A17 17 0 0 1 3 4c0-.6.4-1 1-1h3.5c.6 0 1 .4 1 1 0 1.3.2 2.5.6 3.6.1.3 0 .7-.2 1z"/></svg>
        555-214-7730
      </li>
      <li>
        <svg viewBox="0 0 24 24" aria-hidden="true"><path d="M7 1h10a2 2 0 0 1 2 2v18a2 2 0 0 1-2 2H7a2 2 0 0 1-2-2V3a2 2 0 0 1 2-2zm0 3v14h10V4z"/></svg>
        555-309-4482
      </li>
      <li>
        <svg viewBox="0 0 24 24" aria-hidden="true"><path d="M2 5h20v14H2zm2 2v.5l8 5 8-5V7zm0 2.8V17h16V9.8l-8 5z"/></svg>
        hello@korvaneworks.com
      </li>
      <li>
        <svg viewBox="0 0 24 24" aria-hidden="true"><path d="M12 2a10 10 0 1 0 0 20 10 10 0 0 0 0-20zm-1 17.9A8 8 0 0 1 4.2 10L9 14.8V16a2 2 0 0 0 2 2zm6.9-2.5A2 2 0 0 0 16 16h-1v-3a1 1 0 0 0-1-1H8v-2h2a1 1 0 0 0 1-1V7h2a2 2 0 0 0 2-2v-.4a8 8 0 0 1 2.9 12.8z"/></svg>
        www.korvaneworks.com
      </li>
    </ul>
    <p class="contact__abn">ABN 41 208 576 903</p>
  </div>
</section>

<section class="card card--back" aria-label="Business card back">
  <div class="brand"><span class="brand__dot"></span>Korvane Works</div>
  <ul class="services" aria-label="Services">
    <li>Breakdowns</li>
    <li>Field Service</li>
    <li>A/C Systems</li>
    <li>Machine Rewires</li>
    <li>Mine Site Vehicle Fit Outs</li>
  </ul>
</section>

</body>
</html>
```